Letterhead Design Project

Initially, we would like to review our letterheads.

Something simple which uses our corporate imagery well and is nicely balanced.

Please note that I will be following up this letter-head with some customised quote templates and similarly customisable collateral in the next few weeks.

Target Market(s)

Enterprise business

Industry/Entity Type

Quote

Requirements
Must have
• The Norbix7 logo
See www.norbix7.com.au

Our tagline "Enterprise Hosting, Messaging and Server Virtualisation"

Our website address

Ideally in our colour pallette, but will consider submissions which look fantastic and necessitate other colours.

```html
<!DOCTYPE html>
<html lang="en">
<head>
<meta charset="utf-8">
<title>Norbix7 Letterhead</title>
<link rel="stylesheet" href="https://fonts.googleapis.com/css2?family=Arimo:wght@400;700&display=swap">
<style>
  :root {
    --ink: #000000;
    --paper: #ffffff;
    --brand-red: #cf1f2a;
    --rule: #ffffff;
    --canvas: #ffffff;
  }
  * { margin: 0; padding: 0; box-sizing: border-box; }
  html, body { width: 1200px; height: 1000px; overflow: hidden; background: var(--canvas); }
  body { font-family: "Arimo", Arial, sans-serif; position: relative; }

  .letterhead {
    position: absolute; left: 307px; top: 85px; width: 597px; height: 844px;
    background: var(--paper); border: 1px solid var(--ink);
  }
  .masthead {
    position: absolute; left: 0; top: 0; width: 100%; height: 76px; background: var(--ink);
  }
  .brand { position: absolute; left: 29px; top: 20px; display: flex; align-items: center; gap: 6px; }
  .brand-mark { width: 32px; height: 32px; background: var(--brand-red); }
  .brand-name { color: var(--paper); font-weight: 700; font-size: 36px; line-height: 36px; letter-spacing: -1px; }
  .masthead-rule { position: absolute; left: 29px; top: 56px; width: 532px; height: 1px; background: var(--rule); }
  .tagline {
    position: absolute; left: 29px; top: 60px; color: var(--paper); font-size: 8.5px; white-space: nowrap;
  }
  .tagline .site { margin-left: 9px; }

  .contact-title {
    position: absolute; left: 0; width: 100%; top: 720px; text-align: center;
    font-weight: 700; font-size: 14.5px; color: var(--ink);
  }
  .contact-panel {
    position: absolute; left: 19px; top: 742px; width: 555px; height: 74px;
    background: var(--brand-red); border-radius: 10px; color: var(--paper);
    font-size: 8.3px; line-height: 9.8px;
  }
  .pill {
    position: absolute; background: var(--ink); color: var(--paper); font-weight: 700;
    font-size: 8.3px; line-height: 11px; padding: 0 4px; border-radius: 6px; white-space: nowrap;
  }
  .block { position: absolute; white-space: nowrap; }
  .block p { margin: 0; }
  .row { display: flex; }
  .row .key { width: 21px; }
  .email { font-weight: 700; }
</style>
</head>
<body>
  <section class="letterhead">
    <header class="masthead">
      <div class="brand">
        <span class="brand-mark"></span>
        <span class="brand-name">Norbix7</span>
      </div>
      <div class="masthead-rule"></div>
      <p class="tagline">Enterprise Hosting, Messaging and Server Virtualisation<span class="site">www.norbix7.com.au</span></p>
    </header>

    <h2 class="contact-title">Norbix7 Contact Information</h2>
    <footer class="contact-panel">
      <span class="pill" style="left:5px; top:6px;">Norbix7 Pty. Ltd.</span>
      <div class="block" style="left:9px; top:19px;">
        <p>Suite 4, Level 3</p>
        <p>18 Harbour Lane,</p>
        <p>Kellerton, Australia</p>
        <p>VIC - 3990</p>
      </div>

      <span class="pill" style="left:99px; top:6px;">Phone</span>
      <div class="block" style="left:103px; top:19px;">
        <p class="row"><span class="key">VIC:</span>+61 3 9010 4720</p>
        <p class="row"><span class="key">QLD:</span>+61 7 3050 6142</p>
        <p class="row"><span class="key">WA:</span>+61 8 6120 3381</p>
      </div>
      <div class="block" style="left:195px; top:19px;">
        <p class="row"><span class="key" style="width:24px">NSW:</span>+61 2 8020 7314</p>
        <p class="row"><span class="key" style="width:24px">ACT:</span>+61 2 6110 2865</p>
        <p class="row"><span class="key" style="width:24px">SA:</span>+61 8 7030 5196</p>
      </div>
      <span class="pill" style="left:99px; top:47px;">Emergency Response :</span>
      <div class="block" style="left:103px; top:59px;">
        <p>+61 3 9010 4720 Select Voice Menu Option 5</p>
      </div>

      <span class="pill" style="left:288px; top:6px;">Enquiries</span>
      <div class="block" style="left:288px; top:19px;">
        <p>Sales Enquiries</p>
        <p>Billing Enquiries</p>
        <p>Knowledge Base &amp; Trouble Tickets</p>
        <p>Hosting Support Community</p>
      </div>
      <div class="block email" style="left:423px; top:19px;">
        <p>sales@norbix7.com.au</p>
        <p>accounts@norbix7.com.au</p>
        <p>https://support.norbix7.com.au/</p>
        <p>https://support.norbix7.com.au/</p>
      </div>
    </footer>
  </section>
</body>
</html>
```